Harbor Allied BC

I have a baseline business card that I would like to spruce up!

I actually like this business card. I just want to find a way to have all the information below on it and it too look balanced and professional.

Target Market(s)

Small to medium sized companies - Health Insurance Consulting

Industry/Entity Type

Health Insurance

Contact Information for Business Card

The information I would like included on the business card is:

- Harbor Allied Southridge Title and logo
- Tessa Wrenfield
- Business title: Principal
- 4192 Cobalt Ridge Rd Suite D-117 Cedar Hollow, WA 98712
- Employee Benefits Consulting & (Wellness Consulting) optional
- tessa@harboralliedsr.example
- cell: 425-555-0183

Font styles to use
Other font styles liked:
• I like the font it is currently in but am open to others.

Requirements
Must have
• I like the logo and the color scheme. I even like the layout. I just need to fine tune it!

```html
<!DOCTYPE html>
<html lang="en">
<head>
<meta charset="utf-8">
<title>Harbor Allied Southridge – Business Card</title>
<link href="https://fonts.googleapis.com/css2?family=Lato:wght@300;400;700&display=swap" rel="stylesheet">
<style>
  :root {
    --brand-green: #0c9a57;
    --brand-green-deep: #0a8a4d;
    --pattern-green: #2f8a5f;
    --ink: #1c1c1c;
    --paper: #ffffff;
    --backdrop: #bdbdbd;
    --rule-light: rgba(255,255,255,0.6);
  }
  * { box-sizing: border-box; margin: 0; padding: 0; }
  html, body { width: 1200px; height: 837px; overflow: hidden; }
  body {
    background: var(--backdrop);
    font-family: "Lato", Arial, sans-serif;
    display: flex;
    align-items: center;
    justify-content: center;
    gap: 60px;
  }
  .card {
    width: 500px;
    height: 286px;
    position: relative;
    overflow: hidden;
    box-shadow: 0 6px 18px rgba(0,0,0,0.18);
  }

  /* Front */
  .card-front {
    background: linear-gradient(135deg, var(--brand-green-deep), var(--brand-green) 60%, var(--brand-green-deep));
    color: var(--paper);
  }
  .front-lockup {
    position: absolute;
    left: 58px;
    top: 104px;
    display: flex;
    align-items: center;
    gap: 18px;
  }
  .brand-dot {
    width: 48px; height: 48px;
    border-radius: 50%;
    background: var(--paper);
    flex: none;
  }
  .wordmark {
    font-weight: 400;
    text-transform: uppercase;
    letter-spacing: 0.04em;
    line-height: 1.1;
  }
  .wordmark .wm-main { display: block; font-size: 22px; }
  .wordmark .wm-sub { display: block; font-size: 12px; letter-spacing: 0.18em; text-align: right; }
  .front-divider {
    width: 1px;
    height: 62px;
    background: var(--rule-light);
    margin-left: 4px;
  }
  .front-tagline {
    font-weight: 300;
    font-size: 13px;
    line-height: 1.25;
  }

  /* Back */
  .card-back { background: var(--paper); color: var(--ink); }
  .pattern-area {
    position: absolute;
    left: 0; top: 0;
    width: 170px; height: 286px;
    background: linear-gradient(160deg, var(--pattern-green), var(--brand-green));
  }
  .back-wordmark {
    position: absolute;
    right: 34px;
    top: 40px;
    color: var(--ink);
  }
  .back-wordmark .wm-main { font-size: 18px; }
  .back-wordmark .wm-sub { font-size: 10px; }
  .contact-block {
    position: absolute;
    left: 206px;
    top: 112px;
    font-size: 12.5px;
    line-height: 1.35;
  }
  .person-name { font-size: 19px; font-weight: 300; line-height: 1.1; }
  .person-name strong { font-weight: 700; }
  .person-title { color: var(--brand-green); font-weight: 700; font-size: 13px; margin-bottom: 10px; }
  .address { margin-bottom: 10px; }
  .label { color: var(--brand-green); font-weight: 700; }
</style>
</head>
<body>
  <section class="card card-front" aria-label="Card front">
    <div class="front-lockup">
      <span class="brand-dot" aria-hidden="true"></span>
      <div class="wordmark">
        <span class="wm-main">Harbor Allied</span>
        <span class="wm-sub">Southridge</span>
      </div>
      <span class="front-divider" aria-hidden="true"></span>
      <p class="front-tagline">Employee<br>Benefits<br>Services</p>
    </div>
  </section>

  <section class="card card-back" aria-label="Card back">
    <div class="pattern-area" role="img" aria-label="Green brand pattern panel"></div>
    <div class="wordmark back-wordmark">
      <span class="wm-main">Harbor Allied</span>
      <span class="wm-sub">Southridge</span>
    </div>
    <div class="contact-block">
      <p class="person-name">Tessa <strong>Wrenfield</strong></p>
      <p class="person-title">Principal</p>
      <p class="address">4192 Cobalt Ridge Rd Suite D-117<br>Cedar Hollow, WA 98712</p>
      <p><span class="label">Email:</span> tessa@harboralliedsr.example</p>
      <p><span class="label">Cell:</span> 425-555-0183</p>
    </div>
  </section>
</body>
</html>
```